Design a New Site for a very cool Watch

We have the overall design element of the website and the banners in the PSD file. We need someone to finish our design in PSD and than convert to HTML. We have included the instructions, PSD file, images and all text.

We currently use Hubspot to host and make changes to our site. The entire design aspect is complete so all we need is some minor changes and additions within the photoshop design and than the coding into HTML.

Please only sign up if you understand photoshop and HTML conversion

Here is the DropBox link to the files
https://files.quorvel-share.net/s/pm4kx82lwq7dtne/Belthor%20Site.zip
Updates

We have the basic design concept in Photoshop.  We just need someone who can complete some changes, make some additions and convert to HTML

Target Market(s)

Watch Buyers

Requirements
Must have
• Must look like a professional luxury brand

Our brand colors are very basic with Black, White and Grey can be used

```html
<!DOCTYPE html>
<html lang="en">
<head>
<meta charset="utf-8">
<title>Belthor &amp; Co. — Iconic Timepieces</title>
<link rel="stylesheet" href="https://fonts.googleapis.com/css2?family=Open+Sans:wght@400;600;700&family=Arimo:wght@400&display=swap">
<style>
  :root {
    --ink: #2b2b2b;
    --bar: #333333;
    --black: #0b0a10;
    --grey: #a9a9a9;
    --mid-grey: #8a8a8a;
    --line: #d9d9d9;
    --card: #fdf0ef;
    --card-edge: #ead8d6;
    --blush: #fdf8f8;
    --red: #e02020;
    --white: #ffffff;
  }
  * { box-sizing: border-box; margin: 0; padding: 0; }
  html, body { width: 1024px; height: 1200px; overflow: hidden; background: var(--white); }
  body { position: relative; font-family: "Arimo", Arial, sans-serif; color: var(--ink); }
  .abs { position: absolute; }

  .top-rule { left: 0; top: 0; width: 1024px; height: 5px; background: var(--ink); }
  .utility-nav { left: 82px; top: 12px; display: flex; gap: 19px; font-family: "Open Sans", sans-serif; font-size: 10px; }
  .utility-right { right: 80px; top: 12px; display: flex; align-items: center; font-size: 10px; }
  .utility-right .shop-link { color: var(--red); padding-right: 10px; border-right: 1px solid #bbb; margin-right: 12px; }

  .brand { left: 0; width: 1024px; top: 48px; display: flex; justify-content: center; align-items: center; gap: 10px;
           font-family: "Open Sans", sans-serif; font-size: 19px; font-weight: 400; letter-spacing: 1px; color: var(--ink); }
  .brand .mark { width: 16px; height: 16px; border: 1.5px solid var(--ink); }

  .dash { left: 0; width: 1024px; border-top: 1px dashed var(--line); }

  .main-nav { left: 0; top: 112px; width: 1024px; height: 30px; background: var(--bar); }
  .main-nav ul { list-style: none; display: flex; position: absolute; left: 84px; top: 0; height: 30px; align-items: center;
                 font-size: 10px; color: var(--white); text-transform: uppercase; }
  .main-nav li { margin-right: 24px; display: flex; align-items: center; gap: 16px; }
  .main-nav .search { position: absolute; left: 740px; top: 0; width: 181px; height: 30px; background: #4a4a4a;
                      color: #888; font-size: 10px; padding: 9px 13px; }
  .main-nav .search-btn { position: absolute; left: 920px; top: 0; width: 30px; height: 30px; background: #111; }

  .hero { left: 0; top: 172px; width: 1024px; height: 323px; background: var(--black); overflow: hidden; }
  .hero-photo { position: absolute; left: 560px; top: 0; width: 464px; height: 323px;
                background: radial-gradient(ellipse at 45% 50%, #3a3f5a 0%, #1d2140 35%, #0e1030 60%, #0b0a10 85%); }
  .hero-copy { position: absolute; left: 162px; top: 116px; color: var(--white); font-family: "Open Sans", sans-serif; }
  .hero-copy h1 { font-size: 15px; font-weight: 600; letter-spacing: .8px; line-height: 20px; text-transform: uppercase; margin-bottom: 15px; }
  .hero-copy p { font-size: 12.5px; font-weight: 600; line-height: 15px; width: 300px; }
  .hero-arrow { position: absolute; top: 137px; width: 40px; height: 39px; background: #1f1f24; }
  .hero-dots { position: absolute; left: 442px; top: 298px; display: flex; gap: 5px; }
  .hero-dots span { width: 9px; height: 9px; border-radius: 50%; background: #666; }
  .hero-dots span.on { background: var(--white); }
  .hero-base { left: 0; top: 495px; width: 1024px; height: 7px; background: #7d7d7d; }

  .blush-band { left: 0; top: 770px; width: 1024px; height: 341px; background: var(--blush); }

  .feature { top: 551px; width: 202px; height: 232px; background: var(--card); border: 1px solid var(--card-edge);
             border-bottom: 8px solid var(--grey); text-align: center; font-family: "Open Sans", sans-serif;
             font-size: 11px; letter-spacing: .4px; line-height: 17px; text-transform: uppercase; color: var(--ink); }
  .feature .badge { width: 98px; height: 98px; border-radius: 50%; background: #f8f8f8; border: 1px solid #e2e2e2;
                    box-shadow: 0 1px 3px rgba(0,0,0,.12); margin: 34px auto 27px; display: flex; align-items: center; justify-content: center; }

  .section-rule { left: 0; top: 829px; width: 1024px; border-top: 1px solid #e8e2e2; }
  .about-title { left: 73px; top: 851px; font-family: "Open Sans", sans-serif; font-size: 13px; text-transform: uppercase; }
  .about-photo { left: 73px; top: 888px; width: 203px; height: 102px;
                 background: linear-gradient(90deg, #6b5a4c 0%, #a79b8f 35%, #3b3330 60%, #7a6252 100%); }
  .about-text { left: 298px; top: 894px; width: 192px; font-size: 10px; line-height: 13.7px; color: #555; }
  .about-text a { color: var(--red); text-decoration: none; display: block; }
  .touch { left: 540px; top: 885px; width: 170px; text-align: center; font-family: "Open Sans", sans-serif;
           font-size: 17px; font-weight: 600; color: #3d3d3d; }
  .social { left: 746px; top: 935px; width: 195px; height: 38px; background: #eeeaea; display: flex; align-items: center;
            justify-content: space-around; padding: 0 6px; }
  .social span { width: 28px; height: 28px; border-radius: 50%; background: #c9c5c5; }
  .base-bar { top: 1032px; height: 6px; background: var(--grey); }

  .footer { left: 0; top: 1111px; width: 1024px; height: 89px; background: var(--bar); color: var(--white); text-align: center; }
  .footer ul { list-style: none; display: flex; justify-content: center; gap: 28px; margin-top: 31px; font-size: 10px; letter-spacing: .3px; text-transform: uppercase; }
  .footer .copyright { margin-top: 12px; font-size: 9.5px; color: #ddd; }
</style>
</head>
<body>
  <div class="abs top-rule"></div>
  <nav class="abs utility-nav"><span>My Account</span><span>Collection</span><span>Lifestyle</span><span>Shop now</span></nav>
  <div class="abs utility-right"><span class="shop-link">shop.belthor.com</span><span>Sign in - Register</span></div>

  <div class="abs brand"><span class="mark"></span><span>BELTHOR &amp; CO.</span></div>
  <div class="abs dash" style="top:97px"></div>

  <nav class="abs main-nav">
    <ul>
      <li>Home</li>
      <li>Products <svg width="6" height="8" viewBox="0 0 6 8"><path d="M1 1l3 3-3 3" stroke="#fff" stroke-width="1.6" fill="none"/></svg></li>
      <li>Articles <svg width="6" height="8" viewBox="0 0 6 8"><path d="M1 1l3 3-3 3" stroke="#fff" stroke-width="1.6" fill="none"/></svg></li>
      <li>Photo Gallery <svg width="6" height="8" viewBox="0 0 6 8"><path d="M1 1l3 3-3 3" stroke="#fff" stroke-width="1.6" fill="none"/></svg></li>
      <li>Blog</li>
      <li>Contact</li>
    </ul>
    <div class="search">SEARCH</div>
    <div class="search-btn"><svg width="30" height="30" viewBox="0 0 30 30"><circle cx="13" cy="13" r="4.5" stroke="#fff" stroke-width="2" fill="none"/><path d="M16.5 16.5l5 5" stroke="#fff" stroke-width="3"/></svg></div>
  </nav>
  <div class="abs dash" style="top:156px"></div>

  <section class="abs hero">
    <div class="hero-photo" role="img" aria-label="Close-up photograph of a square steel watch with a dark dial and blue strap"></div>
    <div class="hero-copy">
      <h1>Belthor &amp; Co strives to create<br>iconic timepieces</h1>
      <p>we will always push our limits on developing unique works of wearable art that bend the rules on what a Timepiece can become.</p>
    </div>
    <div class="hero-arrow" style="left:57px"><svg width="40" height="39" viewBox="0 0 40 39"><path d="M22 16l-3 3.5 3 3.5" stroke="#ddd" stroke-width="1.4" fill="none"/></svg></div>
    <div class="hero-arrow" style="left:927px"><svg width="40" height="39" viewBox="0 0 40 39"><path d="M18 16l3 3.5-3 3.5" stroke="#ddd" stroke-width="1.4" fill="none"/></svg></div>
    <div class="hero-dots"><span></span><span class="on"></span><span></span><span></span><span></span></div>
  </section>
  <div class="abs hero-base"></div>

  <div class="abs blush-band"></div>

  <article class="abs feature" style="left:73px">
    <div class="badge"><svg width="56" height="56" viewBox="0 0 56 56" fill="#8a8a8a"><path d="M32 22l4 10 11 1-8 7 3 11-10-6-10 6 3-11-8-7 11-1z"/><path d="M16 6l3 6 6 .5-4.5 4 1.5 6.5-6-3.5-6 3.5 1.5-6.5L7 12.5l6-.5z"/><path d="M40 10l1.5 3.5 3.5.3-2.7 2.4.8 3.6-3.1-2-3.1 2 .8-3.6-2.7-2.4 3.5-.3z"/></svg></div>
    The Orin Story
  </article>
  <article class="abs feature" style="left:298px">
    <div class="badge"><svg width="60" height="50" viewBox="0 0 60 50"><rect x="10" y="6" width="40" height="28" rx="2" fill="#8a8a8a"/><rect x="13" y="9" width="34" height="22" fill="#eee"/><text x="30" y="23" font-family="Arimo, sans-serif" font-size="6.5" fill="#777" text-anchor="middle">REGISTER</text><path d="M4 36h52l-4 6H8z" fill="#8a8a8a"/></svg></div>
    Register your<br>watch
  </article>
  <article class="abs feature" style="left:523px">
    <div class="badge"><svg width="66" height="60" viewBox="0 0 66 60" fill="none" stroke="#8a8a8a"><rect x="11" y="4" width="14" height="10" rx="2" stroke-width="3"/><rect x="11" y="46" width="14" height="10" rx="2" stroke-width="3"/><circle cx="18" cy="30" r="14" stroke-width="4"/><path d="M18 30v-8M18 30l5 4" stroke-width="2"/><circle cx="47" cy="20" r="6" stroke-width="5" stroke-dasharray="3 2"/><circle cx="49" cy="40" r="4.5" stroke-width="4" stroke-dasharray="2.5 1.5"/></svg></div>
    Repair, maintenance<br>&amp; warrenty info
  </article>
  <article class="abs feature" style="left:748px">
    <div class="badge"><svg width="72" height="40" viewBox="0 0 72 40"><path d="M4 18l14-10 50 6-4 22-52-6z" fill="#777"/><circle cx="14" cy="18" r="2.5" fill="#eee"/><text x="42" y="28" font-family="Open Sans, sans-serif" font-weight="700" font-size="13" fill="#fff" text-anchor="middle" transform="rotate(8 42 24)">New</text></svg></div>
    Register to find out about<br>new watch colections
  </article>

  <div class="abs section-rule"></div>
  <h2 class="abs about-title" style="font-weight:400">Belthor &amp; Co</h2>
  <div class="abs about-photo" role="img" aria-label="Photograph of a brand ambassador standing beside a promotional poster"></div>
  <p class="abs about-text">Lorem ipsum dolor sit amet, consectetur adipisicing elit, sed do eiusmod tempor incididunt ut labore et dolore magna aliqua. Ut enim ad minim veniam, quis nostrud exercitation ullamco laboris nisi ut aliquip ex ea commodo consequat.<a href="#">www.belthor.com</a></p>

  <div class="abs touch">
    <svg width="80" height="62" viewBox="0 0 80 62"><path d="M12 30a28 18 0 0 0 56 0a28 14 0 0 1-56 0z" fill="#555"/><path d="M14 30a26 17 0 0 0 52 0" stroke="#555" stroke-width="5" fill="none"/><rect x="28" y="8" width="24" height="20" fill="#eee" stroke="#555" stroke-width="2"/><path d="M28 8l12 10 12-10" stroke="#555" stroke-width="2" fill="none"/></svg>
    <div>KEEP IN TOUCH</div>
  </div>
  <div class="abs social" aria-label="Social links"><span></span><span></span><span></span><span></span><span></span></div>

  <div class="abs base-bar" style="left:73px; width:427px"></div>
  <div class="abs base-bar" style="left:523px; width:428px"></div>
  <div class="abs dash" style="top:1095px"></div>

  <footer class="abs footer">
    <ul><li>Belthor &amp; Company</li><li>Contact us</li><li>Terms of service</li><li>Refund policy</li><li>Privacy policy</li></ul>
    <p class="copyright">Copyright © 2013 Belthor &amp; Co<sup style="font-size:6px">TM</sup></p>
  </footer>
</body>
</html>
```